KitVarro.com FACELIFT design for the online store

A) GENERAL
We need a small FACELIFT design with a short styleguide for our online store http://KitVarro.com (online store for sport goods; the store is just now in responsive design; actually only in German). The store is the first online store worldwide with 3d images for all products.
B) Designers: PLEASE NOTE:
- We don't want change functionality!
- We only want a small facelift.
- We don't need a fully coded website.
C) We only need for the responsive design views:
1. the home page design (one page)
http://www.kitvarro.com/de/
2. the category listing design (one page)
http://www.kitvarro.com/de/alle/running.html
3. the product detail page (one page)
http://www.kitvarro.com/de/pembrik-tz-flo-3d-hvx-herren-traillaufschuhe-drelon-wex.html
4. the cms page (textonly !!!)
http://www.kitvarro.com/de/versand-und-lieferung
5. the Mega drop down
D) We intend to change/use:
- maybe to use a background image in the start page, and each category
- change the header
- change the font sizes for the titles (maybe in capital letters)
- change the mega drop down
Europe
Store
4 page

```html
<!DOCTYPE html>
<html lang="en">
<head>
<meta charset="utf-8">
<title>KitVarro.com – Mega drop down</title>
<link rel="stylesheet" href="https://fonts.googleapis.com/css2?family=Roboto:wght@400;500&display=swap">
<style>
  :root {
    --ink: #000;
    --text: #333;
    --muted: #777;
    --grey-text: #666;
    --panel: #f4f4f4;
    --panel-border: #888;
    --accent: #f0440f;
    --badge: #d4127a;
    --white: #fff;
    --rule: #e2e2e2;
  }
  html, body { margin: 0; padding: 0; width: 1200px; height: 1200px; overflow: hidden; background: var(--white); }
  body { font-family: "Roboto", Arial, sans-serif; color: var(--ink); }
  .stage { position: relative; width: 1000px; height: 1000px; transform: scale(1.2); transform-origin: 0 0; }
  .abs { position: absolute; white-space: nowrap; }

  .util { font-size: 12.5px; color: var(--muted); line-height: 14px; }
  .util-rule { left: 20px; top: 32px; width: 960px; height: 1px; background: var(--rule); }

  .brand { left: 32px; top: 46px; font-size: 31px; line-height: 36px; color: var(--ink); font-weight: 400; letter-spacing: 1px; }

  .search { left: 368px; top: 55px; width: 358px; height: 27px; border: 1px solid #aaa; }
  .search span { position: absolute; left: 8px; top: 7px; font-size: 11.5px; color: #bbb; }
  .search-btn { left: 728px; top: 55px; width: 36px; height: 29px; background: var(--accent); }

  .bag-label { left: 888px; top: 73px; font-size: 12px; line-height: 14px; }

  .main-nav { left: 20px; top: 114px; width: 446px; height: 36px; background: var(--ink); }
  .main-nav .item { position: absolute; top: 11px; color: var(--white); font-size: 14px; font-weight: 500; line-height: 16px; }

  .bar { left: 20px; width: 960px; height: 3px; background: var(--ink); }
  .cat-active { left: 20px; top: 152px; width: 80px; height: 49px; background: var(--panel); }
  .cat { top: 171px; font-size: 13.5px; line-height: 16px; }

  .mega { left: 21px; top: 204px; width: 852px; height: 405px; background: var(--panel); border: 1px solid var(--panel-border); }
  .divider { top: 204px; width: 1px; height: 407px; background: var(--panel-border); }
  .head { font-size: 13px; line-height: 15px; color: var(--ink); }
  .link { font-size: 13.5px; line-height: 16px; color: var(--text); letter-spacing: 0.2px; }

  .offers-title { left: 689px; top: 231px; font-size: 18px; line-height: 20px; color: var(--accent); }
  .product-img { left: 685px; top: 268px; width: 169px; height: 171px; border: 1px solid #bbb; background: radial-gradient(circle at 55% 50%, #2a2a2a 0 35%, #c8e020 36% 48%, #f6f6f6 49%); }
  .badge { left: 687px; top: 275px; width: 48px; height: 28px; border: 1px solid var(--badge); background: var(--white); color: var(--badge); font-size: 16px; font-weight: 500; text-align: center; line-height: 28px; }
  .prod-cat { left: 689px; top: 464px; font-size: 13px; line-height: 15px; }
  .prod-name { left: 689px; top: 485px; font-size: 13px; line-height: 17px; color: var(--grey-text); white-space: normal; width: 170px; }
  .price { left: 691px; top: 524px; font-size: 18px; line-height: 20px; }
</style>
</head>
<body>
<div class="stage">
  <!-- utility bar -->
  <svg class="abs" style="left:686px;top:9px" width="16" height="16" viewBox="0 0 24 24"><path d="M12 2l3 7 7.5.6-5.7 4.9 1.8 7.4L12 18l-6.6 3.9 1.8-7.4L1.5 9.6 9 9z" fill="#666"/></svg>
  <div class="abs util" style="left:705px;top:11px">WISHLIST</div>
  <svg class="abs" style="left:786px;top:11px" width="19" height="12" viewBox="0 0 19 12"><rect width="19" height="4" fill="#000"/><rect y="4" width="19" height="4" fill="#dd0000"/><rect y="8" width="19" height="4" fill="#ffce00"/></svg>
  <div class="abs util" style="left:811px;top:10px">GERMANY</div>
  <svg class="abs" style="left:873px;top:12px" width="13" height="9" viewBox="0 0 13 9"><path d="M1 1l5.5 6L12 1" stroke="#555" stroke-width="1.8" fill="none"/></svg>
  <div class="abs util" style="left:896px;top:10px">SIGN IN</div>
  <div class="abs util-rule"></div>

  <!-- header -->
  <div class="abs brand">KitVarro.com</div>
  <div class="abs search"><span>Search for products</span></div>
  <svg class="abs search-btn" viewBox="0 0 36 29"><circle cx="20" cy="12" r="5" stroke="#fff" stroke-width="2" fill="none"/><path d="M16.5 15.5l-5 5" stroke="#fff" stroke-width="2.4"/></svg>
  <svg class="abs" style="left:909px;top:43px" width="18" height="19" viewBox="0 0 18 19"><rect x="1" y="6" width="16" height="13" fill="#000"/><path d="M5 8V5a4 4 0 0 1 8 0v3" stroke="#000" stroke-width="1.8" fill="none"/></svg>
  <div class="abs bag-label">MY BAG (0)</div>

  <!-- main navigation -->
  <nav class="abs main-nav">
    <svg class="abs" style="left:17px;top:6px" width="22" height="20" viewBox="0 0 22 20"><path d="M11 1L1 10h3v9h5v-6h4v6h5v-9h3z" fill="#fff"/></svg>
    <span class="item" style="left:61px">MEN</span>
    <span class="item" style="left:111px">WOMEN</span>
    <span class="item" style="left:185px">CHILDREN/YOUTH</span>
    <span class="item" style="left:326px">GIFT IDEAS</span>
  </nav>
  <div class="abs bar" style="top:149px"></div>
  <div class="abs cat-active"></div>
  <svg class="abs" style="left:43px;top:151px" width="10" height="5" viewBox="0 0 10 5"><path d="M0 0h10L5 5z" fill="#000"/></svg>

  <div class="abs cat" style="left:21px">OUTDOOR</div>
  <div class="abs cat" style="left:102px">ROCK CLIMBING</div>
  <div class="abs cat" style="left:224px">RUNNING</div>
  <div class="abs cat" style="left:304px">BIKE</div>
  <div class="abs cat" style="left:353px">SKI &amp; FREERIDE</div>
  <div class="abs cat" style="left:471px">SKI TOURING</div>
  <div class="abs cat" style="left:572px">FITNESS</div>
  <div class="abs cat" style="left:646px">FASHION</div>
  <div class="abs cat" style="left:722px">DIGITAL</div>
  <div class="abs cat" style="left:792px">REMAINING STOCK</div>
  <div class="abs cat" style="left:933px">DEALS</div>
  <div class="abs bar" style="top:201px"></div>

  <!-- mega drop down -->
  <div class="abs mega"></div>
  <div class="abs divider" style="left:226px"></div>
  <div class="abs divider" style="left:454px"></div>
  <div class="abs divider" style="left:674px"></div>

  <div class="abs head" style="left:54px;top:230px">OUTDOOR CLOTHING</div>
  <div class="abs link" style="left:55px;top:254px">Jackets</div>
  <div class="abs link" style="left:55px;top:278px">Sweater</div>
  <div class="abs link" style="left:55px;top:302px">Shirts and Shirts</div>
  <div class="abs link" style="left:55px;top:326px">Functional clothing</div>
  <div class="abs link" style="left:55px;top:350px">Pants</div>
  <div class="abs link" style="left:55px;top:374px">Gloves</div>
  <div class="abs link" style="left:55px;top:398px">Socks</div>
  <div class="abs link" style="left:55px;top:422px">Rainwear</div>
  <div class="abs link" style="left:55px;top:446px">Hats &amp; Headbands</div>

  <div class="abs head" style="left:258px;top:228px">SHOES &amp; STICKS</div>
  <div class="abs link" style="left:258px;top:255px">Sneakers</div>
  <div class="abs link" style="left:258px;top:279px">Trekking Shoes</div>
  <div class="abs link" style="left:258px;top:303px">Walking shoes</div>
  <div class="abs link" style="left:258px;top:327px">Mountain Shoes</div>
  <div class="abs link" style="left:258px;top:351px">Walking sticks</div>
  <div class="abs head" style="left:259px;top:412px">BACKPACKS &amp; HEADLAMPS</div>
  <div class="abs link" style="left:261px;top:440px">Backpacks</div>
  <div class="abs link" style="left:261px;top:464px">Headlights</div>

  <div class="abs head" style="left:499px;top:225px">TENTS</div>
  <div class="abs link" style="left:499px;top:252px">2-man tents</div>
  <div class="abs link" style="left:499px;top:276px">3 Man Tents</div>
  <div class="abs link" style="left:499px;top:300px">4-man tents</div>
  <div class="abs head" style="left:498px;top:345px">CAMPING</div>
  <div class="abs link" style="left:498px;top:370px">Sleeping</div>
  <div class="abs link" style="left:498px;top:394px">Matting</div>
  <div class="abs link" style="left:498px;top:418px">Bivouac sacks</div>
  <div class="abs link" style="left:498px;top:442px">Others</div>
  <div class="abs head" style="left:498px;top:487px">WINTER HIKING</div>
  <div class="abs link" style="left:498px;top:515px">Snowshoes</div>
  <div class="abs link" style="left:498px;top:539px">Sticks</div>
  <div class="abs link" style="left:498px;top:563px">Headlights</div>

  <div class="abs offers-title">TOP OFFERS</div>
  <div class="abs product-img" role="img" aria-label="Product photo: black fleece hoody with lime green sleeves and orange zip pocket"></div>
  <div class="abs badge">NEU</div>
  <div class="abs prod-cat">MEN’S OUTDOOR</div>
  <div class="abs prod-name">Alpivex Fleece hoody Zip neck sweater</div>
  <div class="abs price">€ 159,99</div>
</div>
</body>
</html>
```